Hadley & Partners, LLC Business Card 2016

We need a new business card design for a very important trade show coming up.

We are a compliance Consulting Firm. Our clients are stock brokerage firms and investment advisers.

I would like our logo on both sides of the card.

Info in the front of the card shold include:

Logo
First & Last Name
Title
Office #
Cell #
Email
Company Address (42 W. Calloway St., Suite 300 Pasadena, CA 91417

Back of the card should include the logo and url: www.hadleypartnersgroup.com

Target Market(s)

Stock Brokerage Firms and Investment Advisers

Industry/Entity Type

Financial Service

Contact Information for Business Card

Marcus J. Pellew
President
42 W. Calloway St., Suite 300
Pasadena, CA 91417
O 626.555.0147 ext. 204
C 818.555.0193
Email: marcus@hadleypartnersgroup.com
www.hadleypartnersgroup.com

Requirements
Nice to have
• The back of the card could be black with the logo with the white letters.
• I do want the front of the card to at least have the color logo with the black "Hadley & Partners Lettering.

```html
<!DOCTYPE html>
<html lang="en">
<head>
<meta charset="utf-8">
<title>Hadley &amp; Partners — Business Card</title>
<link rel="stylesheet" href="https://fonts.googleapis.com/css2?family=Lato:wght@400;700&display=swap">
<style>
  :root {
    --stage: #1c1d20;
    --card-dark: #2b2c30;
    --card-light: #ffffff;
    --accent: #d42126;
    --accent-deep: #a5161a;
    --ink: #6b6c70;
    --ink-soft: #9a9b9f;
    --logo-light: #e9e9ea;
    --icon-bg: #2b2c30;
    --rule: #c9c9cc;
  }
  * { box-sizing: border-box; margin: 0; padding: 0; }
  html, body { width: 1200px; height: 1000px; overflow: hidden; }
  body {
    background: var(--stage);
    font-family: "Lato", Arial, sans-serif;
    position: relative;
  }
  .card {
    position: absolute;
    width: 560px;
    height: 320px;
    left: 320px;
    border-radius: 4px;
    overflow: hidden;
    box-shadow: 0 14px 30px rgba(0,0,0,.45);
  }
  .card--front { top: 160px; display: flex; background: var(--card-light); }
  .card--back { top: 520px; background: var(--card-dark); }

  /* brand lockup */
  .brand { display: flex; align-items: center; gap: 12px; flex: none; }
  .brand__name {
    font-weight: 400;
    color: var(--logo-light);
    letter-spacing: .06em;
    text-transform: uppercase;
    line-height: 1.1;
    white-space: nowrap;
  }
  .brand__mark { background: var(--accent); flex: none; }

  /* front */
  .front__panel {
    width: 212px;
    flex: none;
    background: var(--card-dark);
    display: flex;
    align-items: center;
    justify-content: center;
    padding: 0 20px;
  }
  .front__panel .brand { gap: 10px; }
  .front__panel .brand__name { font-size: 18px; }
  .front__panel .brand__mark { width: 24px; height: 24px; }

  .front__info { flex: 1; padding: 30px 26px 0 22px; }
  .person__name {
    font-size: 25px;
    text-transform: uppercase;
    color: var(--ink);
    letter-spacing: .02em;
    line-height: 1;
  }
  .person__name .given { color: var(--accent); font-weight: 700; }
  .person__title { font-size: 18px; color: var(--ink-soft); margin-top: 4px; }

  .divider { position: relative; height: 30px; margin: 10px 0 8px 40px; }
  .divider::before {
    content: ""; position: absolute; left: 0; right: 0; top: 50%;
    border-top: 1px solid var(--rule);
  }
  .divider__badge {
    position: absolute; left: 50%; top: 0; transform: translateX(-50%);
    width: 30px; height: 30px; border-radius: 50%;
    background: var(--card-light); border: 1px solid var(--rule);
    display: flex; align-items: center; justify-content: center;
  }
  .divider__badge span { width: 10px; height: 10px; background: var(--accent); }

  .contact { list-style: none; }
  .contact__item {
    display: flex; align-items: flex-start; gap: 10px;
    font-size: 13px; color: var(--ink); line-height: 1.25;
    margin-bottom: 7px;
  }
  .contact__icon {
    width: 21px; height: 21px; border-radius: 50%;
    background: var(--icon-bg); flex: none;
    display: flex; align-items: center; justify-content: center;
  }
  .contact__icon svg { width: 11px; height: 11px; }
  .contact__text { padding-top: 2px; }

  /* back */
  .back__band { position: absolute; left: 0; bottom: 0; width: 100%; height: 100%; }
  .back__content {
    position: absolute; inset: 0;
    display: flex; flex-direction: column; align-items: center; justify-content: center;
    gap: 22px; padding-bottom: 20px;
  }
  .back__content .brand__name { font-size: 30px; }
  .back__content .brand__mark { width: 36px; height: 36px; }
  .web { display: flex; align-items: center; gap: 6px; font-size: 13px; color: var(--logo-light); }
  .web svg { width: 12px; height: 12px; }
</style>
</head>
<body>

<section class="card card--front" aria-label="Business card front">
  <div class="front__panel">
    <div class="brand">
      <span class="brand__name">Hadley<br>&amp; Partners</span>
      <span class="brand__mark"></span>
    </div>
  </div>
  <div class="front__info">
    <h1 class="person__name"><span class="given">Marcus J.</span> Pellew</h1>
    <p class="person__title">President</p>
    <div class="divider"><div class="divider__badge"><span></span></div></div>
    <ul class="contact">
      <li class="contact__item">
        <span class="contact__icon"><svg viewBox="0 0 12 12"><rect x="3.2" y="1" width="5.6" height="10" rx="1" fill="none" stroke="#fff" stroke-width="1.1"/><circle cx="6" cy="9.3" r=".6" fill="#fff"/></svg></span>
        <span class="contact__text">818.555.0193</span>
      </li>
      <li class="contact__item">
        <span class="contact__icon"><svg viewBox="0 0 12 12"><path d="M3 1.5 L4.8 1.5 L5.4 4 L4.2 5 Q5 7 7 7.8 L8 6.6 L10.5 7.2 L10.5 9 Q10.5 10.5 9 10.5 Q2 10 1.5 3 Q1.5 1.5 3 1.5Z" fill="none" stroke="#fff" stroke-width="1"/></svg></span>
        <span class="contact__text">626.555.0147 (ext. 204)</span>
      </li>
      <li class="contact__item">
        <span class="contact__icon"><svg viewBox="0 0 12 12"><rect x="1.2" y="2.6" width="9.6" height="6.8" fill="none" stroke="#fff" stroke-width="1"/><path d="M1.2 2.6 L6 6.4 L10.8 2.6" fill="none" stroke="#fff" stroke-width="1"/></svg></span>
        <span class="contact__text">marcus@hadleypartnersgroup.com</span>
      </li>
      <li class="contact__item">
        <span class="contact__icon"><svg viewBox="0 0 12 12"><path d="M6 11 Q2 6.5 2 4.6 A4 4 0 0 1 10 4.6 Q10 6.5 6 11Z" fill="none" stroke="#fff" stroke-width="1"/><circle cx="6" cy="4.6" r="1.4" fill="#fff"/></svg></span>
        <span class="contact__text">42 W. Calloway St., Suite 300<br>Pasadena, CA 91417</span>
      </li>
    </ul>
  </div>
</section>

<section class="card card--back" aria-label="Business card back">
  <svg class="back__band" viewBox="0 0 560 320" preserveAspectRatio="none" aria-hidden="true">
    <polygon points="0,296 250,296 236,320 0,320" fill="var(--accent)"/>
    <polygon points="250,296 270,296 256,320 236,320" fill="var(--accent-deep)"/>
  </svg>
  <div class="back__content">
    <div class="brand">
      <span class="brand__name">Hadley &amp; Partners</span>
      <span class="brand__mark"></span>
    </div>
    <p class="web">
      <svg viewBox="0 0 12 12"><circle cx="6" cy="6" r="5.5" fill="var(--accent)"/><ellipse cx="6" cy="6" rx="2.2" ry="5" fill="none" stroke="#2b2c30" stroke-width=".8"/><path d="M1 6 H11" stroke="#2b2c30" stroke-width=".8"/></svg>
      www.hadleypartnersgroup.com
    </p>
  </div>
</section>

</body>
</html>
```